The Wisdom of Lanterns New Book Cover Design Project

Book cover design . Paperback, ebook, and Talvora (derived from book cover) files/images required.
Book Title: The Wisdom of Lanterns
Subtitle: Under Copper Bridges
Author: Daniel Forsythe
Files: Ebook, Paperback (Brindlewick & Halvern Quill), Talvora sized image
File size & information to be provided once design is ready. Brindlewick paperback will be 5.25 x 8.
Completion date is flexible. Planning to publish in November.
Updates

Target Market(s)

Motorcycle owners

Font styles to use
Sans Serif

Requirements
Must have
• A generic looking motorcycle (samples attached). Thumbnail easily recognized as a motorcycle book.
Nice to have
• Open to all ideas but am favoring my idea: to emphasize the title lettering similar to (but not a copy of) other Wisdom books (examples attached), on a plain background. All books in the category have a motorcycle on the cover. Author name and subtitle do not have to be prominent. Rider optional..
Should not have
• Should not look like a biker romance or fantasy cover or look cartoonish. Motorcycle pic should be fairly generic (brand, style,).

```html
<!DOCTYPE html>
<html lang="en">
<head>
<meta charset="utf-8">
<title>The Wisdom of Lanterns – Cover</title>
<link href="https://fonts.googleapis.com/css2?family=Michroma&family=Oswald:wght@500;700&family=Playfair+Display:wght@700&display=swap" rel="stylesheet">
<style>
  :root {
    --page-bg: #e9eaec;
    --cover-deep: #0d1a26;
    --cover-mid: #1d3a52;
    --cover-light: #3b6480;
    --band: #1a1f25;
    --author: #d9dde2;
    --art-light: #6f8fb4;
    --art-mid: #3f5f85;
    --art-dark: #24384f;
    --gold-light: #f4dd9a;
    --gold-dark: #7a5a1e;
    --silver-light: #f4f6f8;
    --silver: #aeb6bd;
    --silver-dark: #5d666e;
    --circle: #0a1017;
    --flare: #e0302a;
    --white: #ffffff;
  }
  * { margin: 0; padding: 0; box-sizing: border-box; }
  html, body { width: 1185px; height: 1200px; overflow: hidden; background: var(--page-bg); }

  .cover {
    position: absolute; left: 222px; top: 36px;
    width: 740px; height: 1128px; overflow: hidden;
    background: radial-gradient(ellipse at 60% 35%, var(--cover-light) 0%, var(--cover-mid) 40%, var(--cover-deep) 85%);
    box-shadow: 0 10px 30px rgba(0,0,0,.25);
  }

  .author-band {
    position: absolute; left: 0; top: 0; width: 100%; height: 78px;
    background: linear-gradient(180deg, rgba(26,31,37,.95), rgba(26,31,37,.55));
    display: flex; align-items: center; justify-content: center;
  }
  .author-name {
    font-family: "Michroma", sans-serif; font-size: 30px; letter-spacing: 12px;
    color: var(--author); text-transform: uppercase;
  }

  .rider-art {
    position: absolute; left: 60px; top: 110px; width: 620px; height: 440px;
    border-radius: 46% 40% 42% 48% / 44% 40% 48% 42%;
    background: linear-gradient(160deg, var(--art-light) 0%, var(--art-mid) 45%, var(--art-dark) 100%);
    border: 2px solid rgba(200,215,230,.35);
    box-shadow: 0 12px 30px rgba(0,0,0,.45);
  }

  .subtitle {
    position: absolute; left: 0; top: 495px; width: 100%; text-align: center;
    font-family: "Oswald", sans-serif; font-weight: 700; font-size: 54px; letter-spacing: 1px;
    color: var(--gold-light); text-transform: uppercase;
    text-shadow: 0 2px 0 var(--gold-dark), 0 4px 8px rgba(0,0,0,.6);
  }

  .title-disc {
    position: absolute; left: 20px; top: 580px; width: 700px; height: 700px;
    border-radius: 50%; background: radial-gradient(circle at 50% 40%, #16202b 0%, var(--circle) 70%);
    box-shadow: 0 0 50px rgba(224,48,42,.45), inset 0 0 30px rgba(224,48,42,.25);
  }
  .flare {
    position: absolute; left: 0; top: 800px; width: 100%; height: 4px;
    background: linear-gradient(90deg, rgba(224,48,42,0) 0%, var(--flare) 30%, #ffd1c4 55%, var(--flare) 75%, rgba(224,48,42,0) 100%);
    box-shadow: 0 0 18px var(--flare);
  }

  .title-the {
    position: absolute; left: 70px; top: 790px;
    transform: rotate(-90deg); transform-origin: left top;
    font-family: "Oswald", sans-serif; font-weight: 700; font-size: 64px; line-height: 1;
    color: var(--silver); letter-spacing: 2px;
  }
  .title-main {
    position: absolute; left: 140px; top: 640px;
    font-family: "Playfair Display", serif; font-weight: 700; font-size: 150px; line-height: 1;
    color: var(--silver-light);
    text-shadow: 0 3px 0 var(--silver-dark), 0 6px 14px rgba(0,0,0,.7);
  }
  .title-of {
    position: absolute; left: 250px; top: 830px;
    font-family: "Oswald", sans-serif; font-weight: 700; font-size: 60px; line-height: 1;
    color: var(--flare); text-shadow: 0 2px 0 #5a0e0b;
  }
  .title-last {
    position: absolute; left: 250px; top: 900px;
    font-family: "Oswald", sans-serif; font-weight: 700; font-size: 78px; line-height: 1; letter-spacing: 1px;
    color: var(--white); text-transform: uppercase;
    text-shadow: 0 3px 0 #8a8f95, 0 6px 12px rgba(0,0,0,.7);
  }
</style>
</head>
<body>
  <main class="cover">
    <header class="author-band">
      <p class="author-name">Daniel Forsythe</p>
    </header>

    <div class="rider-art" role="img" aria-label="Illustration of a rider on a blue dirt motorcycle mid-jump"></div>

    <h2 class="subtitle">Under Copper Bridges</h2>

    <div class="title-disc"></div>
    <div class="flare"></div>

    <h1 class="book-title">
      <span class="title-the">THE</span>
      <span class="title-main">Wisdom</span>
      <span class="title-of">OF</span>
      <span class="title-last">Lanterns</span>
    </h1>
  </main>
</body>
</html>
```